Masterfolien & mehr | Branche Gesundheit | Anschlussaufträge
Tolle Leistung, netter Kontakt, verdienter Gewinner!
Zielgruppe
Sonnquell ist Dienstleister im Bereich 'Betriebliches Gesundheitsmanagement'. Zielgruppe sind Unternehmen zahlreicher Branchen, die die Gesundheit ihrer Mitarbeiter untersuchen und verbessern wollen.
Aufgabenstellung
Bitte möglichst Startfolie, Folie mit Aufzählungen und Text und Folie mit Bild und Text und Kontaktfolie.
Beispieltexte und eine entsprechende Folienansicht habe ich beigefügt, das könnte helfen.
Die Präsentation soll als E-Mail-Anhang im Nachgang eines Akquiseanrufs genutzt werden und über Produkte und Lösungen informieren.
Bitte Farbgebung berücksichtigen. Blau: 90/51/0/0, grau dunkel: 68/51/58/30, grau hell: 40/33/49/1
Schriften: Offen für Vorschläge, möglichst freie Schriften oder klassische Linotype.
Wir würden den Gewinner gern mit weiteren Aufträgen versehen, z.B. die Vorlage mit vorgegebenen Inhalten füllen, Flussdiagramme erstellen, Schaubilder erstellen etc..

```html
<!DOCTYPE html>
<html lang="de">
<head>
<meta charset="utf-8">
<title>Zielgruppe Pharmareferenten?</title>
<link href="https://fonts.googleapis.com/css2?family=Roboto+Condensed:ital,wght@1,700&family=Arimo:wght@400;700&display=swap" rel="stylesheet">
<style>
  :root {
    --blue: #0a6ab5;
    --gray-dark: #4a4f4c;
    --gray-light: #a89f88;
    --text: #1c1c1c;
    --white: #ffffff;
  }
  html, body { margin: 0; padding: 0; overflow: hidden; }
  body { width: 1200px; height: 848px; background: var(--white); font-family: "Arimo", Arial, sans-serif; color: var(--text); }
  .slide { position: relative; width: 1200px; height: 848px; overflow: hidden; }

  .title-band { position: absolute; left: 0; top: 53px; width: 983px; height: 84px; background: var(--blue); }
  .title-band .chevron { position: absolute; left: 0; top: 29px; }
  .title-band h1 {
    margin: 0; position: absolute; left: 52px; top: 14px;
    font-family: "Roboto Condensed", "Arial Narrow", sans-serif; font-style: italic; font-weight: 700;
    font-size: 44px; line-height: 56px; color: var(--white); letter-spacing: 0.2px;
  }

  .brand { position: absolute; left: 1010px; top: 72px; width: 140px; text-align: center; }
  .brand .dot { display: block; width: 22px; height: 22px; border-radius: 50%; background: var(--gray-dark); margin: 0 auto 8px; }
  .brand .name { font-family: "Arimo", Arial, sans-serif; font-weight: 700; font-size: 22px; color: var(--gray-dark); }

  .intro { position: absolute; left: 54px; top: 210px; margin: 0; font-size: 21px; line-height: 30px; }
  .intro strong { font-weight: 700; }

  .reasons { position: absolute; left: 53px; top: 363px; width: 929px; height: 341px; box-sizing: border-box; border: 2px solid var(--gray-light); border-top: none; }
  .reasons-head { height: 60px; margin: 0 -2px; background: var(--blue); color: var(--white); font-weight: 700; font-size: 21px; line-height: 60px; padding-left: 34px; }
  .reasons ul { list-style: none; margin: 0; padding: 27px 0 0 0; }
  .reasons li { position: relative; padding-left: 32px; font-size: 15.5px; line-height: 23px; margin-bottom: 26px; }
  .reasons li svg { position: absolute; left: -2px; top: 3px; }

  .footer { position: absolute; top: 778px; font-family: "Roboto Condensed", "Arial Narrow", sans-serif; font-style: italic; font-weight: 700; font-size: 15px; color: var(--gray-dark); }
  .footer.left { left: 54px; }
  .footer.page { left: 1112px; width: 36px; text-align: right; }
</style>
</head>
<body>
<div class="slide">
  <header class="title-band">
    <svg class="chevron" width="14" height="26" viewBox="0 0 14 26"><path d="M0 0 L13 13 L0 26 Z" fill="#ffffff"/></svg>
    <h1>Zielgruppe Pharmareferenten?</h1>
  </header>

  <div class="brand"><span class="dot"></span><span class="name">Sonnquell</span></div>

  <p class="intro">Vertriebsmitarbeiter fühlen sich oftmals nicht angesprochen<br>von den gesundheitsfördernden Angeboten des Betriebes<br><strong>Gründe</strong> dafür können sein:</p>

  <section class="reasons">
    <div class="reasons-head">MÖGLICHE GRÜNDE:</div>
    <ul>
      <li><svg width="12" height="18" viewBox="0 0 12 18"><path d="M0 0 L12 9 L0 18 Z" fill="#0a6ab5"/></svg>Mangelnde Erreichbarkeit: die Angebote werden häufig nur im Unternehmen und in unmittelbarer Nähe<br>angeboten</li>
      <li><svg width="12" height="18" viewBox="0 0 12 18"><path d="M0 0 L12 9 L0 18 Z" fill="#0a6ab5"/></svg>Nicht zielgruppenspezifisch: die Berufsgruppe der Pharmareferenten nimmt nicht dieselben Belastungen<br>wie z.B. ein Büro- oder Labormitarbeiter wahr</li>
      <li><svg width="12" height="18" viewBox="0 0 12 18"><path d="M0 0 L12 9 L0 18 Z" fill="#0a6ab5"/></svg>Nicht vereinbar mit den Arbeitszeiten: die Angebote können oftmals nicht flexibel genutzt werden</li>
      <li><svg width="12" height="18" viewBox="0 0 12 18"><path d="M0 0 L12 9 L0 18 Z" fill="#0a6ab5"/></svg>individuelle und zielgruppenspezifische gesundheitsfördernde Maßnahmen sind notwendig</li>
    </ul>
  </section>

  <div class="footer left">SONNQUELL UG | 2018</div>
  <div class="footer page">03</div>
</div>
</body>
</html>
```